Banner Ad Design Project

We I need three call to action buttons for my new web site. The site is a medical supply company. that should equal 1030x280. The site buttons should say:

1- "EVERYDAY FREE SHIPPING on orders over $50. No code. No hassle."
2- "Call us for FREE EXPERT ADVICE. Click to learn more."
3- "Learn about our QLT Program. Click to continue"

The site is brontawick.com, I need them to replace the flash banner on the home page. I have proper placement, but need them to be distinct colors so they get noticed.

Thank you!

```html
<!DOCTYPE html>
<html lang="en">
<head>
<meta charset="utf-8">
<title>Brontawick – Medical Supplies</title>
<link href="https://fonts.googleapis.com/css2?family=Arimo:wght@400;700&family=Oswald:wght@500;700&family=Lobster&display=swap" rel="stylesheet">
<style>
:root{
  --page:#f2f2f2;
  --white:#ffffff;
  --line:#d9d9d9;
  --ink:#222222;
  --muted:#777777;
  --link:#1a8fd8;
  --blue-hi:#2aa3f0;
  --blue-lo:#0a66c4;
  --green-hi:#a8e6a0;
  --green-lo:#22a250;
  --yellow-hi:#fde58a;
  --yellow-lo:#e3ac12;
  --sky-hi:#22bff2;
  --sky-lo:#0a78d6;
  --red:#ee1c1c;
  --lime:#f6f05a;
  --dark-btn:#3c3c3c;
  --gold:#f7c21c;
}
*{box-sizing:border-box;margin:0;padding:0}
html,body{width:1200px;height:762px;overflow:hidden;background:var(--page);font-family:"Arimo",Arial,sans-serif;color:var(--ink)}
.site{position:relative;width:1200px;height:762px}
.column{position:absolute;left:109px;top:0;width:966px;height:762px;background:var(--white)}
.abs{position:absolute}

/* top bar */
.topbar{left:119px;top:9px;width:956px;height:33px;border:1px solid var(--line);border-radius:3px;background:linear-gradient(#fdfdfd,#ececec)}
.account-links{position:absolute;right:6px;top:4px;display:flex;gap:2px}
.account-links a{display:flex;align-items:center;gap:6px;height:24px;padding:0 9px;border:1px solid var(--line);background:linear-gradient(#fff,#eee);font-size:11.5px;font-weight:700;color:#8a8a8a;text-decoration:none}
.account-links svg{width:14px;height:14px}

/* header */
.brand{left:109px;top:66px;height:58px;display:flex;align-items:center;gap:10px}
.brand-mark{width:40px;height:40px;background:#1b1b1b}
.brand-name{font-family:"Arimo",Arial,sans-serif;font-weight:700;font-size:44px;color:#1f80c8;letter-spacing:-1px}
.helpline{left:700px;top:68px;width:375px;height:55px;background:linear-gradient(#38b8f5,#0757b8);display:flex;align-items:center}
.helpline .agent{width:48px;height:55px;background:linear-gradient(#f6dccb,#c9d8e8)}
.helpline .ask{font-family:"Lobster",cursive;color:var(--white);font-size:19px;line-height:23px;margin-left:22px;width:135px}
.helpline .call{font-family:"Lobster",cursive;color:var(--gold);font-size:24px;line-height:26px;text-align:center}
.searchbar{left:109px;top:125px;width:966px;height:55px;border-radius:4px 4px 0 0;background:linear-gradient(var(--blue-hi),var(--blue-lo))}
.searchbar label{position:absolute;left:534px;top:13px;font-size:21px;color:var(--white)}
.searchbar .field{position:absolute;left:616px;top:5px;width:300px;height:36px;background:var(--white);border-radius:3px;font-size:11px;color:#999;padding:11px 16px;box-shadow:inset 0 1px 3px rgba(0,0,0,.25)}
.searchbar .go{position:absolute;left:922px;top:5px;width:38px;height:36px;border-radius:3px;background:linear-gradient(#2f8fe0,#0c5cb4);display:flex;align-items:center;justify-content:center}

/* categories */
.categories{left:109px;top:205px;width:966px;height:112px;display:flex}
.cat{position:relative;width:96.6px;height:112px}
.cat .tile{position:absolute;left:0;top:34px;width:100%;height:78px;border:1px solid var(--line);border-right:none;background:linear-gradient(#fff,#f3f3f3)}
.cat:last-child .tile{border-right:1px solid var(--line)}
.cat .pic{position:absolute;left:20px;top:3px;width:56px;height:58px;border-radius:6px}
.cat .name{position:absolute;left:2px;right:2px;top:72px;text-align:center;font-size:11.5px;line-height:15px;font-weight:700;text-decoration:underline;color:var(--ink)}

/* promo buttons */
.promo{top:338px;width:306px;height:228px;border-radius:12px;overflow:hidden;box-shadow:0 8px 6px -4px rgba(0,0,0,.35)}
.promo h2{position:absolute;z-index:2;left:22px;top:12px;font-family:"Oswald","Arial Narrow",sans-serif;font-weight:700;font-size:35px;line-height:37px;color:var(--white);text-shadow:1px 2px 2px rgba(0,0,0,.35);letter-spacing:-.3px}
.promo h2 .hot{color:var(--red)}
.shipping{left:108px;background:linear-gradient(160deg,var(--green-hi),var(--green-lo) 70%)}
.shipping .sub{position:absolute;left:26px;top:91px;font-size:14px;color:var(--white)}
.shipping .tag{position:absolute;left:21px;top:138px;font-family:"Oswald","Arial Narrow",sans-serif;font-weight:700;font-size:25px;line-height:25px;color:var(--lime)}
.shipping .art{position:absolute;left:162px;top:90px;width:128px;height:120px;border-radius:8px;background:linear-gradient(#e4b24a,#9a6418)}
.advice{left:429px;background:linear-gradient(160deg,var(--yellow-hi),var(--yellow-lo) 75%)}
.advice .phone{position:absolute;left:80px;top:92px}
.advice .art{position:absolute;left:192px;top:96px;width:108px;height:132px;border-radius:10px 10px 0 0;background:linear-gradient(#f4d7b8,#2a62b8 50%)}
.cta{position:absolute;z-index:2;border:2px solid var(--white);border-radius:10px;font-family:"Oswald","Arial Narrow",sans-serif;font-weight:700;color:var(--white);text-align:center;text-shadow:1px 1px 2px rgba(0,0,0,.35)}
.advice .cta{left:29px;top:129px;width:152px;height:78px;background:linear-gradient(#6fd27a,#2ea44a);font-size:22px;line-height:25px;padding-top:12px}
.program{left:750px;background:linear-gradient(160deg,var(--sky-hi),var(--sky-lo) 75%)}
.program .art{position:absolute;left:112px;top:92px;width:102px;height:72px;border-radius:6px;background:linear-gradient(#3a3a3a,#9fc3d6)}
.program .cta{left:52px;top:144px;width:218px;height:55px;background:linear-gradient(#f9d55c,#e0a60e);font-size:23px;line-height:51px}

/* lower row */
.cart-box{left:146px;top:592px;width:216px;height:107px;border:1px solid var(--line);background:var(--white)}
.cart-box .head{height:42px;border-bottom:1px solid var(--line);display:flex;align-items:center;gap:14px;padding-left:10px;background:linear-gradient(#fff,#f4f4f4)}
.cart-box .icon{width:24px;height:24px;border-radius:3px;background:#1c6fc4;display:flex;align-items:center;justify-content:center}
.cart-box h3{font-size:13.5px;font-weight:700;color:#333}
.cart-box p{padding:17px 0 0 19px;font-size:11.5px;line-height:15px;color:#222}
.cart-box p b{color:#1c5aa8}
.product{top:592px;width:216px;height:144px;border:1px solid #cfcfcf;background:linear-gradient(#fff,#f2f2f2)}
.product h4{margin-top:11px;text-align:center;font-size:13px;line-height:16px;font-weight:400;color:var(--link)}
.product .pic{position:absolute;left:52px;top:44px;width:96px;height:90px;border-radius:6px;background:linear-gradient(#e9e9e9,#bdbdbd)}
.product .buy{position:absolute;right:9px;bottom:9px;width:85px;height:28px;border-radius:2px;background:var(--dark-btn);color:var(--white);font-size:13.5px;font-weight:700;text-align:center;line-height:28px}
</style>
</head>
<body>
<div class="site">
  <div class="column"></div>

  <div class="abs topbar">
    <nav class="account-links">
      <a href="#"><svg viewBox="0 0 14 14"><circle cx="7" cy="4.5" r="3.2" fill="#c8742a"/><path d="M1 14c0-4 3-6 6-6s6 2 6 6z" fill="#2a5ea8"/></svg>My Account</a>
      <a href="#"><svg viewBox="0 0 14 14"><path d="M1 2h2l2 7h7l1-5H4" fill="none" stroke="#777" stroke-width="1.4"/><circle cx="6" cy="12" r="1.2" fill="#777"/><circle cx="11" cy="12" r="1.2" fill="#777"/></svg>My Cart</a>
      <a href="#"><svg viewBox="0 0 14 14"><path d="M1 2h2l2 7h7l1-5H4" fill="none" stroke="#777" stroke-width="1.4"/><path d="M8 5h5M11 3l2 2-2 2" stroke="#1c6fc4" stroke-width="1.6" fill="none"/></svg>Checkout</a>
    </nav>
  </div>

  <div class="abs brand"><span class="brand-mark"></span><span class="brand-name">brontawick</span></div>

  <div class="abs helpline">
    <div class="agent" role="img" aria-label="Photo of a customer service agent with headset"></div>
    <div class="ask">Questions?<br>Need Help?</div>
    <div class="call">Call Us At:<br>(555) 014-2290</div>
  </div>

  <div class="abs searchbar">
    <label>Search:</label>
    <div class="field">Search entire store here...</div>
    <div class="go"><svg width="16" height="16" viewBox="0 0 16 16"><circle cx="6.5" cy="6.5" r="4.5" fill="none" stroke="#fff" stroke-width="2.2"/><path d="M10 10l4 4" stroke="#fff" stroke-width="2.6" stroke-linecap="round"/></svg></div>
  </div>

  <nav class="abs categories">
    <div class="cat"><div class="tile"></div><div class="pic" role="img" aria-label="Walker product photo" style="background:linear-gradient(#f2f2f2,#b5b5b5)"></div><div class="name">Walkers and Rollators</div></div>
    <div class="cat"><div class="tile"></div><div class="pic" role="img" aria-label="Toilet safety frame product photo" style="background:linear-gradient(#fafafa,#c9c9c9)"></div><div class="name">Bathroom Equipment</div></div>
    <div class="cat"><div class="tile"></div><div class="pic" role="img" aria-label="Crutches product photo" style="background:linear-gradient(#eaeaea,#555)"></div><div class="name">Canes and Crutches</div></div>
    <div class="cat"><div class="tile"></div><div class="pic" role="img" aria-label="Wheelchair product photo" style="background:linear-gradient(#cfcfcf,#3d3d3d)"></div><div class="name">Standard and Power Wheelchairs</div></div>
    <div class="cat"><div class="tile"></div><div class="pic" role="img" aria-label="Medical stool product photo" style="background:linear-gradient(#555,#c9c9c9)"></div><div class="name">Furniture and Supplies</div></div>
    <div class="cat"><div class="tile"></div><div class="pic" role="img" aria-label="Blue exam gloves product photo" style="background:linear-gradient(#5ea8ec,#1f5fc0)"></div><div class="name">Gloves and Masks</div></div>
    <div class="cat"><div class="tile"></div><div class="pic" role="img" aria-label="Underpad product photo" style="background:linear-gradient(#e4f3fb,#a9d6ef)"></div><div class="name">Incontinence</div></div>
    <div class="cat"><div class="tile"></div><div class="pic" role="img" aria-label="Hospital bed product photo" style="background:linear-gradient(#a8826a,#5a3e30)"></div><div class="name">Beds and Mattresses</div></div>
    <div class="cat"><div class="tile"></div><div class="pic" role="img" aria-label="Pedal exerciser product photo" style="background:linear-gradient(#e8e8e8,#444)"></div><div class="name">Personal Care</div></div>
    <div class="cat"><div class="tile"></div><div class="name">More<br>Categories</div></div>
  </nav>

  <a class="abs promo shipping" href="#">
    <h2>EVERYDAY <span class="hot">FREE</span><br>SHIPPING!</h2>
    <div class="sub">on orders over $50</div>
    <div class="tag">No code.<br>No hassle.</div>
    <div class="art" role="img" aria-label="Illustration of a cardboard shipping box"></div>
  </a>

  <a class="abs promo advice" href="#">
    <h2>Call us for <span class="hot">FREE</span><br>EXPERT ADVICE</h2>
    <svg class="phone" width="40" height="26" viewBox="0 0 40 26"><path d="M3 9c0-6 34-6 34 0v3h-9V8H12v4H3z" fill="#fff"/><path d="M9 12h22l4 12H5z" fill="#fff"/><circle cx="20" cy="18" r="3.5" fill="#e3ac12"/></svg>
    <div class="art" role="img" aria-label="Illustration of a waving customer advisor in a blue suit"></div>
    <div class="cta">Click to learn<br>more...</div>
  </a>

  <a class="abs promo program" href="#">
    <h2 style="left:18px">LEARN ABOUT OUR<br><span class="hot">QLT</span>PROGRAM</h2>
    <div class="art" role="img" aria-label="Illustration of a strip of film frames"></div>
    <div class="cta">Click to continue.</div>
  </a>

  <aside class="abs cart-box">
    <div class="head">
      <span class="icon"><svg width="16" height="14" viewBox="0 0 16 14"><path d="M1 2h2.5l2 7h7.5l1.5-5H4.5" fill="none" stroke="#fff" stroke-width="1.6"/><circle cx="6.5" cy="12" r="1.3" fill="#fff"/><circle cx="12" cy="12" r="1.3" fill="#fff"/></svg></span>
      <h3>MY CART</h3>
    </div>
    <p>You have <b>no items</b> in your<br>shopping cart.</p>
  </aside>

  <div class="abs product" style="left:372px"><h4>Exercise Peddler with<br>Attractive Silver Vein Finish</h4><div class="pic" role="img" aria-label="Pedal exerciser product photo"></div><div class="buy">Buy Now!</div></div>
  <div class="abs product" style="left:597px"><h4>Steerable Knee Walker</h4><div class="pic" role="img" aria-label="Knee walker product photo"></div><div class="buy">Buy Now!</div></div>
  <div class="abs product" style="left:822px"><h4>Adjustable Height Home Bed<br>Assist Handle</h4><div class="pic" role="img" aria-label="Bed assist handle product photo"></div><div class="buy">Buy Now!</div></div>
</div>
</body>
</html>
```